Events & Entertainment Production Coordination Business Cards

We need a business card for a new company based in Los Angeles called "Bright Harbor Works"
Our company brings people together for events and helps coordinate different productions. We bring artists from a different country to perform or do events in the U.S.
We are looking for something fun, lively, colorful, creative, and simple.
Nothing that looks too crisp, dark, stiff, or modern.
We connect people from different parts of the world, so definitely something eye-catching will be great!
Colors we would like to see are Black, Yellow, Red, White, Brown to name a few. (Feel free to use more!)
(Double-sided is an option also)
Business
Contact Information for Business Card
Contact Information to put on Business Card:
Name
Title
Address - 2 lines
Phone - place for 3 numbers
E-mail
URL

```html
<!DOCTYPE html>
<html lang="en">
<head>
<meta charset="utf-8">
<title>Bright Harbor Works – Business Cards</title>
<link href="https://fonts.googleapis.com/css2?family=Lato:ital,wght@0,400;0,700;1,400&display=swap" rel="stylesheet">
<style>
  :root {
    --brand-red: #9e242b;
    --sand: #e6c785;
    --ink: #4a4a4a;
    --paper: #ffffff;
    --crop: #7a7a7a;
  }
  * { margin: 0; padding: 0; box-sizing: border-box; }
  html, body { width: 1200px; height: 1200px; overflow: hidden; background: var(--paper); }
  body { font-family: "Lato", sans-serif; color: var(--ink); }
  .sheet { position: relative; width: 1200px; height: 1200px; }
  .crop-marks { position: absolute; inset: 0; }
  .crop-marks line { stroke: var(--crop); stroke-width: 1; }
  .crop-marks .on-red { stroke: #d9a0a3; }

  .card-front { position: absolute; left: 0; width: 1200px; height: 480px; }
  .card-front.top { top: 0; }
  .card-front.bottom { top: 447px; }

  .logo-box {
    position: absolute; left: 656px; top: 245.6px; width: 117.6px; height: 52.8px;
    background: var(--brand-red); color: var(--paper);
    font-size: 16px; display: flex; align-items: center; justify-content: center;
  }
  .illustration-slot {
    position: absolute; left: 838px; top: 164px; width: 235px; height: 121px;
    background: linear-gradient(90deg, var(--brand-red) 0%, var(--brand-red) 45%, var(--sand) 85%, var(--sand) 100%);
  }
  .company {
    position: absolute; left: 656px; top: 325px; font-size: 10px; line-height: 12px;
  }
  .company-name { font-size: 14.4px; font-weight: 700; line-height: 18px; margin-bottom: 1px; text-transform: uppercase; }
  .label { font-weight: 700; }
  .key { display: inline-block; width: 18px; }

  .person { position: absolute; left: 851px; top: 333px; font-size: 11.5px; line-height: 14px; }
  .person-name { font-size: 16px; font-weight: 700; line-height: 20px; }
  .person-title { font-style: italic; font-size: 10.5px; margin-bottom: 6px; }

  .tagline-band {
    position: absolute; left: 603px; top: 410px; width: 436px; height: 48px;
    background: var(--brand-red); color: var(--paper);
    font-size: 8.8px; text-align: center; padding-top: 11px; letter-spacing: 0.1px;
  }

  .card-back {
    position: absolute; left: 82px; top: 642px; width: 450px; height: 263px;
    background: var(--brand-red); color: var(--paper);
  }
  .card-back .company { left: 39px; top: 45px; color: var(--paper); }
  .card-back .url { position: absolute; left: 39px; top: 141px; font-size: 9.5px; font-weight: 700; }
  .card-back .tagline { position: absolute; left: 39px; top: 204px; font-size: 8.8px; }
</style>
</head>
<body>
<div class="sheet">

  <section class="card-back">
    <div class="company">
      <div class="company-name">Bright Harbor Works</div>
      <div class="label">Head Office</div>
      <div>418 Cedar Lane NW</div>
      <div>Port Alden, LA</div>
      <div><span class="key">T</span>9779-614-2083</div>
      <div><span class="key">F</span>9777-508-3196</div>
    </div>
    <div class="url">www.brightharborworks.com</div>
    <div class="tagline">CONNECTING · PEOPLE · COMMITMENT</div>
  </section>

  <section class="card-front top">
    <div class="logo-box">Your Logo</div>
    <div class="illustration-slot" role="img" aria-label="Illustration area: two arms shaking hands, red sleeve and tan sleeve"></div>
    <div class="company">
      <div class="company-name">Bright Harbor Works</div>
      <div class="label">Head Office</div>
      <div>418 Cedar Lane NW</div>
      <div>Port Alden, LA</div>
      <div><span class="key">T</span>9779-614-2083</div>
      <div><span class="key">F</span>9777-508-3196</div>
    </div>
    <div class="person">
      <div class="person-name">Marisol</div>
      <div class="person-title">Manager</div>
      <div>Mobile:&nbsp; 515-367-902</div>
      <div>marisol@brightharbor.com</div>
    </div>
    <div class="tagline-band">CONNECTING · PEOPLE · COMMITMENT</div>
  </section>

  <section class="card-front bottom">
    <div class="logo-box">Your Logo</div>
    <div class="illustration-slot" role="img" aria-label="Illustration area: two arms shaking hands, red sleeve and tan sleeve"></div>
    <div class="person">
      <div class="person-name">Marisol</div>
      <div class="person-title">Manager</div>
      <div>Mobile:&nbsp; 515-367-902</div>
      <div>marisol@brightharbor.com</div>
    </div>
  </section>

  <svg class="crop-marks" width="1200" height="1200" viewBox="0 0 1200 1200">
    <line x1="617.6" y1="176" x2="617.6" y2="200"/>
    <line x1="1039.2" y1="176" x2="1039.2" y2="200"/>
    <line x1="617.6" y1="458" x2="617.6" y2="476"/>
    <line x1="1039.2" y1="458" x2="1039.2" y2="476"/>
    <line x1="585" y1="208" x2="609" y2="208"/>
    <line x1="1047" y1="208" x2="1073" y2="208"/>
    <line x1="585" y1="442.4" x2="603" y2="442.4"/>
    <line x1="1047" y1="442.4" x2="1073" y2="442.4"/>
    <line x1="617.6" y1="623" x2="617.6" y2="646"/>
    <line x1="1039.2" y1="623" x2="1039.2" y2="646"/>
    <line x1="617.6" y1="899" x2="617.6" y2="923"/>
    <line x1="1039.2" y1="899" x2="1039.2" y2="923"/>
    <line x1="585" y1="656" x2="609" y2="656"/>
    <line x1="1047" y1="656" x2="1073" y2="656"/>
    <line x1="585" y1="890" x2="609" y2="890"/>
    <line x1="1047" y1="890" x2="1073" y2="890"/>
    <line x1="96" y1="623" x2="96" y2="646"/>
    <line x1="518" y1="623" x2="518" y2="646"/>
    <line class="on-red" x1="96" y1="646" x2="96" y2="648"/>
    <line x1="96" y1="905" x2="96" y2="923"/>
    <line x1="518" y1="905" x2="518" y2="923"/>
    <line class="on-red" x1="96" y1="899" x2="96" y2="905"/>
    <line class="on-red" x1="518" y1="899" x2="518" y2="905"/>
    <line x1="63" y1="656" x2="82" y2="656"/>
    <line x1="532" y1="656" x2="551" y2="656"/>
    <line class="on-red" x1="82" y1="656" x2="88" y2="656"/>
    <line class="on-red" x1="526" y1="656" x2="532" y2="656"/>
    <line x1="63" y1="890" x2="82" y2="890"/>
    <line x1="532" y1="890" x2="551" y2="890"/>
    <line class="on-red" x1="82" y1="890" x2="88" y2="890"/>
    <line class="on-red" x1="526" y1="890" x2="532" y2="890"/>
  </svg>
</div>
</body>
</html>
```